Bref créative
Ostravelde German Shepherds
West Bloodline German Shepherds
Bright & Fun-filled
Torsten Ebbelmann
287 Murow Rd
Suite F.
Portland, Tx 79152
torsten@ostravelde-kennel.example
www.ostravelde-kennel.example
Logo blown up, and some creativity.
Heres the logo. If you could make the German Shepherd text black that would be awesome. Currently with it being yellow it doesnt stick out enough. See what you can do. Thanks!
Not sure if zip file works? So just going to do this....

```html
<!DOCTYPE html>
<html lang="en">
<head>
<meta charset="utf-8">
<title>Ostravelde German Shepherds — Business Card</title>
<link href="https://fonts.googleapis.com/css2?family=Arimo:wght@400;700&display=swap" rel="stylesheet">
<style>
  :root {
    --stage: #e9e7e3;
    --card-black: #0f0f0f;
    --panel-white: #ffffff;
    --silhouette-light: #f4f4f4;
    --silhouette-edge: #bdbdbd;
    --gold: #f2b01e;
    --gold-deep: #d99a10;
    --ink: #1a1a1a;
    --ink-soft: #3a3a3a;
    --brand-text: #ffffff;
  }
  * { box-sizing: border-box; margin: 0; padding: 0; }
  html, body { width: 1200px; height: 821px; overflow: hidden; }
  body {
    background: var(--stage);
    font-family: "Arimo", Arial, sans-serif;
    position: relative;
  }
  .card {
    position: absolute;
    width: 560px;
    height: 320px;
    background: var(--card-black);
    overflow: hidden;
    box-shadow: 0 6px 18px rgba(0,0,0,.25);
  }
  .card--front { left: 20px; top: 250px; }
  .card--back  { left: 620px; top: 250px; }

  /* front */
  .front-panel {
    position: absolute; left: 0; top: 0; width: 290px; height: 100%;
    background: var(--panel-white);
  }
  .head-illustration {
    position: absolute; left: 290px; top: 0; width: 50px; height: 100%;
    background: linear-gradient(90deg, var(--silhouette-light) 0%, var(--silhouette-edge) 100%);
  }
  .front-stripe {
    position: absolute; left: 340px; top: 0; right: 0; height: 12px;
    background: linear-gradient(90deg, var(--gold-deep), var(--gold));
    clip-path: polygon(5% 0, 100% 0, 100% 100%, 0 100%);
  }
  .contact { position: absolute; left: 24px; top: 46px; color: var(--ink); }
  .contact__name { font-weight: 700; font-size: 25px; letter-spacing: .1px; white-space: nowrap; }
  .contact__address { margin-top: 26px; font-size: 12px; line-height: 17px; color: var(--ink-soft); }
  .contact__lines { margin-top: 34px; list-style: none; font-size: 12px; color: var(--ink-soft); }
  .contact__lines li { display: flex; align-items: center; gap: 10px; height: 19px; white-space: nowrap; }
  .contact__lines svg { width: 14px; height: 14px; fill: var(--ink); flex: none; }

  .brand {
    position: absolute; display: flex; flex-direction: column; align-items: center;
    color: var(--brand-text); font-weight: 700; text-align: center;
  }
  .brand__mark { background: var(--gold); }
  .brand__name { text-transform: uppercase; line-height: 1.15; }
  .card--front .brand { left: 360px; top: 92px; width: 190px; }
  .card--front .brand__mark { width: 46px; height: 46px; margin-bottom: 12px; }
  .card--front .brand__name { font-size: 18px; letter-spacing: 1px; }
  .card--front .brand__name span { display: block; font-size: 10px; letter-spacing: 2.4px; }

  /* back */
  .back-band {
    position: absolute; left: 0; right: 90px; top: 22px; height: 15px;
    background: linear-gradient(90deg, var(--gold-deep), var(--gold));
    clip-path: polygon(0 0, 100% 0, 97% 100%, 0 100%);
    display: flex; align-items: center; padding-left: 22px;
    font-size: 10px; letter-spacing: 2px; color: var(--ink); font-weight: 700;
  }
  .card--back .brand { left: 0; right: 0; top: 100px; margin: 0 auto; width: 280px; }
  .card--back .brand__mark { width: 62px; height: 62px; margin-bottom: 14px; }
  .card--back .brand__name { font-size: 28px; letter-spacing: 1.5px; }
  .card--back .brand__name span { display: block; font-size: 14px; letter-spacing: 3.6px; }
</style>
</head>
<body>
  <section class="card card--front">
    <div class="front-panel"></div>
    <div class="head-illustration" role="img" aria-label="Illustration area: light silhouette of a German Shepherd head in profile"></div>
    <div class="front-stripe"></div>

    <div class="contact">
      <h1 class="contact__name">Torsten Ebbelmann</h1>
      <p class="contact__address">287 Murow Rd Suite F.<br>Portland, Tx 79152</p>
      <ul class="contact__lines">
        <li><svg viewBox="0 0 16 16"><path d="M3 2h3l1 3-2 1.5a9 9 0 0 0 4.5 4.5L11 9l3 1v3c0 .6-.4 1-1 1A12 12 0 0 1 2 3c0-.6.4-1 1-1z"/></svg>(361) 555-0142</li>
        <li><svg viewBox="0 0 16 16"><path d="M4 1h8v4H4zM2 6h12v6h-2v3H4v-3H2zm3 4v4h6v-4z"/></svg>(361) 555-0187</li>
        <li><svg viewBox="0 0 16 16"><path d="M1 3h14v10H1zm1.5 1.2V5l5.5 4 5.5-4v-.8L8 8z"/></svg>torsten@ostravelde-kennel.example</li>
      </ul>
    </div>

    <div class="brand">
      <div class="brand__mark"></div>
      <p class="brand__name">Ostravelde<span>German Shepherds</span></p>
    </div>
  </section>

  <section class="card card--back">
    <div class="back-band">www.ostravelde-kennel.example</div>
    <div class="brand">
      <div class="brand__mark"></div>
      <p class="brand__name">Ostravelde<span>German Shepherds</span></p>
    </div>
  </section>
</body>
</html>
```